RW Hollis LLC Business Card - Civil Engineering & Consulting Firm

We need a Business Card that is elegant, and masculine.  It is our Professional Civil Engineering & Consulting Company located in San Antonio TX (Not s construction or builder firm- no gears & no tool images please). We provide civil engineering services including  commercial site plans, grading and drainage plans, utility plans, hydraulics and hydrology, land planning, utility coordination, and other general civil engineering services related to commercial and residential development.
We have 2 existing Logos. We would like to convey reliability, strength, trustworthiness and attention to detail.  Blues and orange tones as per logo We are OK with the use of a darker blue in the mix.  We have 2 logo versions - Full Company Name Logo to go on the back of card, & Small Icon Logo for the front w/ personal Info.

Target Market(s)
Architects, Real Estate Developers, Other Strctural Engineers, Surveyers, General Contractors
Industry/Entity Type
Professional Civil Engineering
Contact Information for Business Card
Name, Position, Address, Cell & Office #, email, and company website
Font styles to use
Other font styles liked:
- Avian
Requirements
Should not have
- No Tools, No Gears, no Cranes, or Construction Equipment.

```html
<!DOCTYPE html>
<html lang="en">
<head>
<meta charset="utf-8">
<title>RW Hollis LLC – Business Card</title>
<link rel="stylesheet" href="https://fonts.googleapis.com/css2?family=Josefin+Sans:wght@300;400&family=Arimo:wght@400&display=swap">
<style>
  :root {
    --backdrop: #1d1d1d;
    --card: #0c0c0c;
    --blue: #6fa6dc;
    --orange: #f0922b;
    --text: #d9d9d9;
    --rule: #3a3a3a;
  }
  * { margin: 0; padding: 0; box-sizing: border-box; }
  html, body {
    width: 1200px; height: 900px; overflow: hidden;
    background: radial-gradient(ellipse at 60% 30%, #2c2c2c 0%, var(--backdrop) 60%, #121212 100%);
  }
  .canvas {
    position: relative; width: 1200px; height: 900px;
    display: flex; align-items: center; justify-content: center; gap: 40px;
  }
  .card {
    position: relative; width: 540px; height: 309px;
    background: var(--card);
    box-shadow: 0 18px 40px rgba(0,0,0,.6);
    overflow: hidden;
  }
  /* Front */
  .card-front .brand {
    position: absolute; left: 0; top: 0; width: 185px; height: 100%;
    display: flex; align-items: center; justify-content: center;
    border-right: 1px solid var(--rule);
  }
  .brand-name {
    font-family: "Josefin Sans", sans-serif; font-weight: 300;
    color: var(--blue); font-size: 20px; letter-spacing: 2px;
    text-transform: uppercase; text-align: center; line-height: 1.3;
  }
  .contact {
    position: absolute; left: 215px; top: 62px; right: 20px;
    font-family: "Arimo", sans-serif; color: var(--text);
  }
  .person-name {
    font-family: "Josefin Sans", sans-serif; font-weight: 300;
    font-size: 27px; color: var(--blue); letter-spacing: .5px; line-height: 1;
  }
  .person-name .surname { color: var(--orange); }
  .person-role { font-size: 14px; margin-top: 6px; }
  .contact-list { list-style: none; margin-top: 16px; font-size: 14px; }
  .contact-list li { display: flex; align-items: center; gap: 8px; height: 21px; }
  .contact-list svg { width: 14px; height: 14px; flex: none; }
  .contact-list .accent { color: var(--orange); }
  .address { margin-top: 16px; font-size: 14px; line-height: 1.45; }
  /* Back */
  .card-back .wordmark {
    position: absolute; left: 0; right: 0; top: 96px;
    text-align: center;
  }
  .card-back .brand-name { font-size: 42px; letter-spacing: 5px; }
  .brand-mark {
    display: inline-block; width: 12px; height: 12px; background: var(--orange);
    margin-top: 18px;
  }
  .tagline {
    position: absolute; left: 0; right: 0; bottom: 48px; text-align: center;
    font-family: "Arimo", sans-serif; font-size: 12.5px; letter-spacing: .3px;
    color: var(--blue); text-transform: uppercase;
  }
</style>
</head>
<body>
<main class="canvas">
  <section class="card card-front" aria-label="Business card front">
    <div class="brand"><p class="brand-name">RW Hollis<br>LLC</p></div>
    <div class="contact">
      <h1 class="person-name">DANIEL <span class="surname">MERCER</span></h1>
      <p class="person-role">Managing Director</p>
      <ul class="contact-list">
        <li>
          <svg viewBox="0 0 16 16" aria-hidden="true"><path d="M3 1.5l3 3-1.6 1.8a9 9 0 0 0 5.3 5.3L11.5 10l3 3-2 2C6.5 14.5 1.5 9.5 1 3.5z" fill="none" stroke="var(--blue)" stroke-width="1.4"/></svg>
          210-555 014 382
        </li>
        <li>
          <svg viewBox="0 0 16 16" aria-hidden="true"><rect x="1" y="3" width="14" height="10" fill="var(--blue)"/><path d="M1 3l7 6 7-6" fill="none" stroke="var(--card)" stroke-width="1.2"/></svg>
          office@rwhollis.net
        </li>
        <li>
          <svg viewBox="0 0 16 16" aria-hidden="true"><g fill="none" stroke="var(--blue)" stroke-width="1.2"><circle cx="8" cy="8" r="6.5"/><ellipse cx="8" cy="8" rx="3" ry="6.5"/><path d="M1.5 8h13M2.5 4.8h11M2.5 11.2h11"/></g></svg>
          <span>www.<span class="accent">rwhollis</span>.net</span>
        </li>
      </ul>
      <p class="address">318, Alamo Ridge Drive<br>78205, San Antonio TX</p>
    </div>
  </section>

  <section class="card card-back" aria-label="Business card back">
    <div class="wordmark">
      <p class="brand-name">RW Hollis LLC</p>
      <span class="brand-mark" aria-hidden="true"></span>
    </div>
    <p class="tagline">Commercial and Residential Development</p>
  </section>
</main>
</body>
</html>
```